Prescription Savings Card

Looking to revamp our cards that are distributed to pharmacies. Processing information must stand out and be in black with lines through zeros for easy identification.
I have included some previous card designs for consideration. we are looking to go with something cleaner with mainly processing information on the back similar to all white version attached.
Target Market(s)
Pharmacists and Pharmacy Technicians
Industry/Entity Type
prescription medications
Contact Information for Business Card
processing information
Requirements
Must have
- easy to read processing information

```html
<!DOCTYPE html>
<html lang="en">
<head>
<meta charset="utf-8">
<title>MedPass Savings Card</title>
<link rel="stylesheet" href="https://fonts.googleapis.com/css2?family=Montserrat:wght@300;400;500;600;700;800&family=Roboto+Mono:wght@500;700&display=swap">
<style>
  :root {
    --page: #f5f5f5;
    --card-dark: #020f14;
    --band-dark: #0e1a20;
    --card-light: #ffffff;
    --band-light: #eef0f2;
    --red: #d2262d;
    --blue: #312f96;
    --white: #ffffff;
    --black: #000000;
    --muted: #3a3f44;
  }
  * { margin: 0; padding: 0; box-sizing: border-box; }
  html, body {
    width: 1200px; height: 1057px; overflow: hidden;
    background: var(--page);
    font-family: "Montserrat", sans-serif;
  }
  .card {
    position: absolute; left: 333px;
    width: 533px; height: 304px; overflow: hidden;
  }
  .card--front { top: 205px; background: var(--card-dark); color: var(--white); }
  .card--back { top: 548px; background: var(--card-light); color: var(--black); }
  .card__art { position: absolute; inset: 0; width: 100%; height: 100%; }
  .brand {
    position: absolute; font-weight: 800; line-height: 1; white-space: nowrap;
  }
  .card--front .brand {
    left: 0; right: 0; top: 117px; text-align: center;
    font-size: 66px; letter-spacing: -2px;
  }
  .card--back .brand {
    left: 37px; top: 32px; font-size: 38px; letter-spacing: -1.5px;
  }
  .benefits { position: absolute; left: 38px; top: 90px; list-style: none; }
  .benefits li {
    font-size: 12.5px; font-weight: 600; line-height: 24px; white-space: nowrap;
  }
  .processing {
    position: absolute; left: 362px; top: 92px;
    display: grid; grid-template-columns: 70px 14px auto;
    font-size: 12.5px; line-height: 17.7px; color: var(--black);
  }
  .processing dt { font-weight: 700; }
  .processing .sep { font-weight: 700; }
  .processing dd {
    font-family: "Roboto Mono", monospace;
    font-weight: 700; font-size: 12.5px;
    font-variant-numeric: slashed-zero;
  }
  .notice {
    position: absolute; left: 0; right: 0; top: 212px; text-align: center;
  }
  .notice__title {
    display: inline-block; position: relative; white-space: nowrap;
    font-size: 13px; font-weight: 700; letter-spacing: 4.4px;
    padding: 0 0 7px 4px;
  }
  .notice__title::after {
    content: ""; position: absolute; left: 50%; bottom: 0;
    width: 214px; margin-left: -107px;
    border-bottom: 1px solid var(--black);
  }
  .notice__text {
    font-size: 9px; font-weight: 400; line-height: 13px; margin-top: 7px;
    color: var(--muted); white-space: nowrap;
  }
  .notice__text strong { font-weight: 700; color: var(--black); }
</style>
</head>
<body>

<section class="card card--front">
  <svg class="card__art" viewBox="0 0 533 304" aria-hidden="true">
    <polygon points="0,0 200,0 0,151" fill="var(--band-dark)"/>
    <polygon points="0,0 80,0 0,60" fill="var(--red)"/>
    <polygon points="533,157 533,304 340,304" fill="var(--band-dark)"/>
    <polygon points="533,235 533,304 443,304" fill="var(--blue)"/>
  </svg>
  <div class="brand">MedPass</div>
</section>

<section class="card card--back">
  <svg class="card__art" viewBox="0 0 533 304" aria-hidden="true">
    <polygon points="0,0 218,0 0,168" fill="var(--band-light)"/>
    <polygon points="0,0 99,0 0,75" fill="var(--red)"/>
    <polygon points="533,121 533,304 292,304" fill="var(--band-light)"/>
    <polygon points="533,216 533,304 405,304" fill="var(--blue)"/>
  </svg>
  <div class="brand">MedPass</div>

  <ul class="benefits">
    <li>SAVE UP TO 99%</li>
    <li>100% HIPAA COMPLIANT</li>
    <li>LOWER PRICE GUARANTEE</li>
    <li>COVER 90 DAYS SUPPLY &amp; PET MEDS</li>
  </ul>

  <dl class="processing">
    <dt>BIN</dt><span class="sep">:</span><dd>014120</dd>
    <dt>PCN</dt><span class="sep">:</span><dd>MDPS2</dd>
    <dt>GRP</dt><span class="sep">:</span><dd>MDPASS</dd>
    <dt>ID</dt><span class="sep">:</span><dd>Mp0000</dd>
    <dt>CONDOR</dt><span class="sep">:</span><dd>48217</dd>
  </dl>

  <div class="notice">
    <div class="notice__title">ATTENTION PHARMACY</div>
    <p class="notice__text">
      If You Are Unable To Process A Prescription Through Or Program<br>
      <strong>Please Call (0800)-555-0142</strong><br>
      Administrated By Northway Health - <strong>THIS IS NOT INSURANCE</strong>
    </p>
  </div>
</section>

</body>
</html>
```